BUSINESS CARD DESIGN

NAME- TODD MARSHECK
PHONE NUMER - 808- 555-0147
EMAIL- OFFICE@VORN-GRADEWORKS.COM
BACK OF CARD- SPEACIALIZES IN LAND CLEARING, FORESTRY MUCLHING AND EXCAVATION

Contact Information for Business Card

NAME- TODD MARSHECK PHONE NUMER - 808- 555-0147 EMAIL- OFFICE@VORN-GRADEWORKS.COM BACK OF CARD- SPEACIALIZES IN LAND CLEARING , MUCLHING AND EXCAVATION

```html
<!DOCTYPE html>
<html lang="en">
<head>
<meta charset="utf-8">
<title>Vorn Gradeworks – Business Card</title>
<link href="https://fonts.googleapis.com/css2?family=Montserrat:wght@400;500;700&display=swap" rel="stylesheet">
<style>
  :root {
    --backdrop: #e9e6e1;
    --card-white: #ffffff;
    --card-black: #060606;
    --ink: #111111;
    --accent: #f5a800;
    --emboss: #1a1a1a;
    --emboss-edge: #262626;
    --emboss-text: #3a3a3a;
  }
  html, body {
    margin: 0;
    padding: 0;
    width: 900px;
    height: 1200px;
    overflow: hidden;
    background: var(--backdrop);
    font-family: "Montserrat", sans-serif;
  }
  .canvas {
    position: relative;
    width: 900px;
    height: 1200px;
  }
  .card {
    position: absolute;
    border-radius: 22px;
    box-shadow: 0 6px 18px rgba(0,0,0,0.25);
    overflow: hidden;
  }
  .card-front {
    left: 80px; top: 131px; width: 742px; height: 440px;
    background: var(--card-white);
  }
  .card-back {
    left: 78px; top: 638px; width: 744px; height: 440px;
    background: var(--card-black);
  }
  .brand-mark {
    position: absolute;
    display: flex;
    flex-direction: column;
    align-items: center;
    color: var(--ink);
    font-weight: 700;
    text-align: center;
    white-space: nowrap;
  }
  .brand-mark .dot {
    border-radius: 50%;
    border: 6px solid currentColor;
    box-sizing: border-box;
  }
  .brand-small { left: 53px; top: 24px; width: 236px; letter-spacing: 1px; }
  .brand-small .dot { width: 116px; height: 116px; margin-bottom: 16px; }
  .brand-small .name { font-size: 19px; line-height: 1.35; }
  .brand-large {
    left: 405px; top: 144px; width: 286px; height: 286px;
    justify-content: center;
  }
  .brand-large .ring {
    position: absolute; left: 0; top: 0; width: 286px; height: 286px;
    border-radius: 50%; border: 12px solid var(--ink); box-sizing: border-box;
  }
  .brand-large .name { font-size: 24px; line-height: 1.3; letter-spacing: 1px; position: relative; }
  .person {
    position: absolute; right: 52px; top: 64px; text-align: right;
  }
  .person .full-name {
    margin: 0; color: var(--accent); font-weight: 700; font-size: 25px; letter-spacing: 0.5px;
  }
  .person .role {
    margin: 6px 0 0; color: var(--ink); font-weight: 500; font-size: 16px;
  }
  .contacts {
    position: absolute; left: 44px; top: 322px; margin: 0; padding: 0; list-style: none;
  }
  .contacts li {
    display: flex; align-items: center; height: 28px;
    font-size: 16px; font-weight: 500; color: var(--ink);
  }
  .contacts svg { width: 14px; height: 14px; margin-right: 10px; fill: var(--accent); }
  .brand-faint {
    left: 122px; top: 76px; width: 500px; color: var(--emboss);
    text-shadow: 0 1px 0 var(--emboss-edge); letter-spacing: 2px;
  }
  .brand-faint .dot { width: 166px; height: 166px; margin-bottom: 18px; border-width: 8px; }
  .brand-faint .name { font-size: 26px; line-height: 1.3; }
  .specialties {
    position: absolute; left: 0; right: 0; top: 390px; margin: 0;
    text-align: center; color: var(--emboss-text);
    font-size: 12px; font-weight: 500; letter-spacing: 1.2px;
  }
</style>
</head>
<body>
<main class="canvas">
  <section class="card card-front">
    <div class="brand-mark brand-small">
      <span class="dot"></span>
      <span class="name">VORN GRADEWORKS<br>LLC HAWAII</span>
    </div>

    <div class="person">
      <h1 class="full-name">TODD MARSHECK</h1>
      <p class="role">Managing Director</p>
    </div>

    <ul class="contacts">
      <li>
        <svg viewBox="0 0 24 24"><path d="M6.6 10.8a15.1 15.1 0 0 0 6.6 6.6l2.2-2.2a1 1 0 0 1 1-.25 11.4 11.4 0 0 0 3.6.57 1 1 0 0 1 1 1V20a1 1 0 0 1-1 1A17 17 0 0 1 3 4a1 1 0 0 1 1-1h3.5a1 1 0 0 1 1 1c0 1.25.2 2.45.57 3.57a1 1 0 0 1-.25 1z"/></svg>
        808- 555-0147
      </li>
      <li>
        <svg viewBox="0 0 24 24"><path d="M2 5h20v2l-10 6L2 7z"/><path d="M2 9l10 6 10-6v10H2z"/></svg>
        OFFICE@VORN-GRADEWORKS.COM
      </li>
      <li>
        <svg viewBox="0 0 24 24"><circle cx="12" cy="12" r="10"/></svg>
        WWW.VORN-GRADEWORKS.COM
      </li>
    </ul>

    <div class="brand-mark brand-large">
      <span class="ring"></span>
      <span class="name">VORN<br>GRADEWORKS</span>
    </div>
  </section>

  <section class="card card-back">
    <div class="brand-mark brand-faint">
      <span class="dot"></span>
      <span class="name">VORN GRADEWORKS<br>LLC HAWAII<br>808-555-0147</span>
    </div>
    <p class="specialties">SPECIALIZES IN LAND CLEARING, FORESTRY MULCHING AND EXCAVATION</p>
  </section>
</main>
</body>
</html>
```